Crestline Lending Group Business Cards

We are looking to revamp the current business cards each of our locations uses. We are a lending company that specializes in personal loans, title loans, and tax services. We have locations in New Mexico, Texas, and Oklahoma.

We would like a cleaner, sleeker look while still highlighting what we offer. Title Loans, Personal Loans & Tax Services. We also want to include our referral fee somewhere on the card. We would like to see an English option as well as a Spanish option for the cards.

PLEASE NOTE: Some business cards do not include the employee's name but just the store's location, while others will include both.

These are double-sided business cards, and we would like to see proof if possible. I have included proofs of our current business cards for you to review below, as well as our company logo. Feel free to get creative with the logo, etc! Colors should match the logo; however, you do not need to use all of our logo colors if you don't want to.

```html
<!DOCTYPE html>
<html lang="en">
<head>
<meta charset="utf-8">
<title>Crestline Lending Group – Business Card</title>
<link rel="stylesheet" href="https://fonts.googleapis.com/css2?family=Lato:wght@300;400;700;900&family=Kalam:wght@400&display=swap">
<style>
  :root {
    --green: #0f5030;
    --red: #c1202a;
    --black: #0b0b0b;
    --white: #ffffff;
    --ink: #141414;
    --backdrop: #dcdcdc;
  }
  * { box-sizing: border-box; margin: 0; padding: 0; }
  html, body {
    width: 1200px; height: 801px; overflow: hidden;
    background: var(--backdrop);
    font-family: "Lato", Arial, sans-serif;
  }
  .canvas { position: relative; width: 1200px; height: 801px; }

  .card {
    position: absolute; left: 351px; width: 522px; height: 297px;
    background: var(--white); overflow: hidden;
  }
  .card-front { top: 43px; }
  .card-back { top: 423px; border: 10px solid var(--green); }

  /* front */
  .wave { position: absolute; left: 0; top: 0; width: 522px; height: 265px; }
  .brand { position: absolute; left: 22px; top: 62px; display: flex; align-items: center; gap: 8px; }
  .brand-dot { width: 14px; height: 14px; border-radius: 50%; background: var(--red); }
  .brand-name { color: var(--green); font-weight: 700; font-size: 21px; line-height: 1.1; width: 170px; }
  .brand-web { position: absolute; left: 72px; top: 112px; color: var(--red); font-size: 11.5px; }

  .services { position: absolute; right: 14px; top: 17px; list-style: none; text-align: right; }
  .services li {
    font-weight: 700; font-size: 13px; letter-spacing: 1.2px; color: var(--ink);
    line-height: 18.5px; display: flex; justify-content: flex-end; align-items: center; gap: 9px;
  }
  .services li::after { content: ""; width: 9px; height: 9px; border-radius: 50%; background: var(--red); }

  .person { position: absolute; left: 23px; top: 160px; color: var(--red); font-size: 19px; }
  .person .first { font-weight: 400; }
  .person .last { font-weight: 900; }
  .person::after { content: ""; display: block; width: 30px; height: 2px; background: var(--green); margin-top: 3px; }

  .contact { position: absolute; right: 14px; top: 185px; list-style: none; color: var(--white); }
  .contact li {
    display: flex; justify-content: flex-end; align-items: center; gap: 12px;
    height: 22px; font-size: 13px;
  }
  .contact li.address { font-size: 10.5px; font-weight: 700; letter-spacing: 0.3px; }
  .contact svg { width: 12px; height: 12px; fill: var(--white); }

  .regions {
    position: absolute; left: 0; bottom: 0; width: 100%; height: 32px;
    background: var(--black); display: flex; justify-content: center; align-items: center; gap: 30px;
    color: var(--white); font-weight: 700; font-size: 12px; letter-spacing: 3.2px;
  }
  .regions .sep { width: 9px; height: 9px; border-radius: 50%; background: var(--red); }

  /* back */
  .brush {
    position: absolute; left: 63px; top: 43px; width: 410px; height: 100px;
    background: var(--red); border-radius: 8px 24px 18px 10px;
  }
  .referral-title {
    position: absolute; left: 0; top: 70px; width: 100%; text-align: center;
    font-family: "Kalam", "Comic Sans MS", cursive; color: var(--white); font-size: 34px; letter-spacing: 1px;
    line-height: 46px;
  }
  .referral-lead {
    position: absolute; left: 0; top: 158px; width: 100%; text-align: center;
    font-weight: 700; font-size: 17px; color: var(--ink); line-height: 22px;
  }
  .referral-amount {
    position: absolute; left: 0; top: 180px; width: 100%; text-align: center;
    font-weight: 900; font-size: 46px; color: var(--red); line-height: 56px;
  }
</style>
</head>
<body>
<main class="canvas">

  <section class="card card-front" aria-label="Business card front">
    <svg class="wave" viewBox="0 0 522 265" aria-hidden="true">
      <path fill="var(--green)" d="M0,228 C120,236 200,232 300,200 C380,170 430,110 522,94 L522,265 L0,265 Z"/>
      <path fill="var(--red)" d="M363,154 C420,125 470,108 522,102 L522,118 C470,122 420,136 363,154 Z"/>
      <path fill="var(--red)" d="M0,197 C60,212 120,220 175,222 C120,226 50,222 0,212 Z"/>
    </svg>

    <div class="brand">
      <span class="brand-dot"></span>
      <span class="brand-name">Crestline Lending Group</span>
    </div>
    <p class="brand-web">www.crestlinelending.com</p>

    <ul class="services">
      <li>PERSONAL LOANS</li>
      <li>TITLE LOANS</li>
      <li>TAX SERVICES</li>
    </ul>

    <p class="person"><span class="first">JANE </span><span class="last">DOE</span></p>

    <ul class="contact">
      <li>(505) 555-1212
        <svg viewBox="0 0 24 24"><path d="M6.6 10.8a15.1 15.1 0 0 0 6.6 6.6l2.2-2.2c.3-.3.7-.4 1-.2 1.1.4 2.3.6 3.6.6.6 0 1 .4 1 1V20c0 .6-.4 1-1 1A17 17 0 0 1 3 4c0-.6.4-1 1-1h3.5c.6 0 1 .4 1 1 0 1.3.2 2.5.6 3.6.1.3 0 .7-.2 1z"/></svg>
      </li>
      <li>abcd@crestlinelending.com
        <svg viewBox="0 0 24 24"><path d="M2 5h20v14H2z M2 5l10 8 10-8" fill="var(--white)" stroke="var(--green)" stroke-width="1.6"/></svg>
      </li>
      <li class="address">123 ELM STREET, SUITE B, ANYTOWN, TEXAS 55555
        <svg viewBox="0 0 24 24"><path d="M12 2a7 7 0 0 0-7 7c0 5 7 13 7 13s7-8 7-13a7 7 0 0 0-7-7zm0 9.5A2.5 2.5 0 1 1 12 6.5a2.5 2.5 0 0 1 0 5z"/></svg>
      </li>
    </ul>

    <div class="regions">
      <span>NEW MEXICO</span><span class="sep"></span><span>TEXAS</span><span class="sep"></span><span>OKLAHOMA</span>
    </div>
  </section>

  <section class="card card-back" aria-label="Business card back">
    <div class="brush" role="img" aria-label="Red paint brush stroke behind the referral headline"></div>
    <p class="referral-title">Refer a friend</p>
    <p class="referral-lead">GET UP TO</p>
    <p class="referral-amount">$100</p>
  </section>

</main>
</body>
</html>
```